website design for Brixa Motor Gleam llc. an automotive Dry Ice detailling and cleaning business.

We need a website designed for an automotive detailing/cleaning company. I would like a grayscale style with the chosen colors to accent/highlight. We use super dry, compressed air to propel precisely processed, uniform particles of dry ice to clean and/or remove dirt and contaminants form vehicles concentrating mainly on undercarriage, engine bay and wheels/wheel wells. This process prevents water/moisture getting into areas of the vehicle you don't want it.

Target Market(s)

vehicle owners with luxury and/or collector cars

Industry/Entity Type

automotive dry ice detailing and cleaning

Coding

Coded - Design and coding required

Number of Pages Required

2 page

Font styles to use
Sans Serif

Colors
0054AA
0677BA
7BADD7
CADEEF
E8F1F8
00AB8E
00BBA5
67D7C9
C6EFE9
E9F9F6
EB3D1F
EC4F4E
F09395
F8D3D4
FCEDEE

Requirements
Must have
• logo prominently displayed on a darker background area. Links to social media and other businesses I am associated with. Photos and short video, sync with social so last (how many?3,5?) posts automatically sync with/show up on website.
Nice to have
• mostly grayscale with chosen colors to accentuate or for attention, excitement

```html
<!DOCTYPE html>
<html lang="en">
<head>
<meta charset="utf-8">
<title>Brixa Motor Gleam – Dry Ice Detailing</title>
<link rel="stylesheet" href="https://fonts.googleapis.com/css2?family=Saira+Semi+Condensed:wght@500;600;700&family=Roboto:wght@400;500&display=swap">
<style>
:root{
  --red:#e3101e;
  --blue:#4cbde6;
  --ink:#1b1b1b;
  --text:#3a3a3a;
  --grey-bar:#e3e3e3;
  --grey-footer:#e2e2e2;
  --grey-bottom:#c8c8c8;
  --white:#ffffff;
  --head:"Saira Semi Condensed", sans-serif;
  --body:"Roboto", sans-serif;
}
*{box-sizing:border-box;margin:0;padding:0}
html,body{width:1200px;height:3741px;overflow:hidden}
body{position:relative;background:var(--white);font-family:var(--body);color:var(--text)}
.abs{position:absolute}
a{color:inherit;text-decoration:none}

/* header */
.topbar{left:360px;top:0;width:840px;height:44px;background:var(--grey-bar);clip-path:polygon(0 0,100% 0,100% 100%,40px 100%);font-size:13px;color:var(--ink)}
.topbar .hours{position:absolute;left:207px;top:14px;display:flex;align-items:center;gap:6px}
.social{display:flex;gap:9px}
.social span{width:9px;height:9px;border-radius:50%;background:var(--ink);display:block}
.topbar .social{position:absolute;left:652px;top:17px}
.brand{font-family:var(--head);font-weight:700;color:var(--red);font-size:28px;line-height:1;display:flex;align-items:center;gap:10px;white-space:nowrap}
.brand i{width:18px;height:18px;border-radius:50%;background:var(--blue);display:block;flex:none}
.header-brand{left:115px;top:64px}
.contact-item{display:flex;gap:14px;align-items:center;font-size:13px;color:var(--ink);line-height:1.5;white-space:nowrap}
.contact-item b{font-weight:500;display:block}
.call{left:530px;top:66px}
.mail{left:716px;top:66px}
.btn{display:flex;align-items:center;justify-content:center;border-radius:24px;font-family:var(--head);font-weight:600;color:var(--white);text-transform:uppercase;white-space:nowrap}
.btn-book{left:915px;top:65px;width:173px;height:44px;background:var(--red);font-size:14px;box-shadow:0 4px 8px rgba(0,0,0,.2)}
.underline-red{left:0;top:150px;width:400px;height:5px;background:var(--red)}
.nav{left:360px;top:128px;width:840px;height:45px;background:var(--red);clip-path:polygon(30px 0,100% 0,100% 100%,0 100%);font-family:var(--head);font-weight:600;font-size:13px;color:var(--white);text-transform:uppercase;white-space:nowrap}
.nav a{position:absolute;top:14px}
.nav .active::after{content:"";position:absolute;left:0;right:0;bottom:-5px;height:2px;background:var(--white)}
.nav .tools{position:absolute;left:648px;top:14px;display:flex;gap:14px;align-items:center;font-family:var(--body);font-weight:400;font-size:12.5px}

/* hero */
.hero{left:0;top:155px;width:1200px;height:600px;background:linear-gradient(90deg,#555 0%,#7a7a7a 30%,#3e3e3e 50%,#2b2b2b 70%,#1c1c1c 100%)}
.hero-tag{position:absolute;font-family:var(--head);font-weight:600;font-size:32px;color:var(--white);background:rgba(0,0,0,.45);display:flex;align-items:center}
.tag-before{left:0;top:0;width:262px;height:70px;padding-left:75px}
.tag-after{right:0;bottom:0;width:270px;height:75px;padding-left:92px}
.hero-box{position:absolute;left:218px;top:163px;width:765px;height:264px;border:2px solid var(--white);background:rgba(20,20,20,.72);text-align:center;color:var(--white)}
.hero-box h1{font-family:var(--head);font-weight:600;font-size:60px;line-height:1;margin-top:28px;white-space:nowrap}
.hero-box h1 span{color:var(--blue)}
.hero-box p{font-size:14.5px;line-height:31px;margin:12px auto 0;width:660px}
.btn-start{position:absolute;left:277px;top:180px;width:210px;height:47px;background:var(--red);font-size:15px}
.hero-arrow{position:absolute;top:278px;width:48px;height:47px;background:rgba(0,0,0,.4);display:flex;align-items:center;justify-content:center}

/* section titles */
.section-title{left:0;width:1200px;text-align:center;font-family:var(--head);font-weight:600;font-size:42px;color:var(--ink);line-height:1}
.section-title span{color:var(--red)}
.rule{left:557px;width:86px;height:3px;background:var(--blue)}

/* why choose */
.feature{width:240px}
.feature .icon{width:84px;height:84px;border:1.5px solid var(--red);border-radius:50%;display:flex;align-items:center;justify-content:center}
.feature h3{font-family:var(--head);font-weight:600;font-size:18px;color:var(--ink);margin-top:17px;white-space:nowrap}
.feature p{font-size:12.5px;line-height:24px;margin-top:8px;padding-left:2px}
.why-photo{left:610px;top:958px;width:572px;height:505px;border-radius:50% 50% 50% 50% / 46% 46% 54% 54%;border-top-left-radius:70% 60%;background:radial-gradient(circle at 65% 40%,#9a9a9a 0%,#6a6a6a 45%,#2e2e2e 100%)}

/* focus */
.focus{left:0;top:1543px;width:1200px;height:694px;background:linear-gradient(180deg,#ececec,#e6e6e6)}
.focus-card{position:absolute;top:203px;width:320px;text-align:center}
.focus-card .photo{width:268px;height:268px;border-radius:50%;margin:0 auto;box-shadow:0 6px 14px rgba(0,0,0,.25)}
.focus-card h3{font-family:var(--body);font-weight:500;font-size:15.5px;color:var(--ink);margin-top:28px}
.focus-card p{font-size:13.5px;line-height:26px;margin-top:6px}

/* process */
.step-num{font-family:var(--head);font-weight:500;font-size:128px;line-height:1;color:transparent;-webkit-text-stroke:3px #7e9fb6}
.step-label{font-family:var(--head);font-weight:600;font-size:29px;color:var(--ink);text-align:center;line-height:37px;width:260px}

/* appointment */
.appt{left:0;top:2746px;width:598px;height:516px;background:#f3f3f3}
.appt h2{position:absolute;left:110px;top:58px;font-family:var(--head);font-weight:600;font-size:40px;color:var(--ink);white-space:nowrap}
.appt .rule-left{position:absolute;left:112px;top:125px;width:88px;height:3px;background:var(--blue)}
.field{position:absolute;background:var(--white);border:1px solid #b8b8b8;font-size:13px;color:#555;padding:18px 9px 0}
.field.select::after{content:"";position:absolute;right:14px;top:22px;width:6px;height:6px;border-right:1.3px solid #555;border-bottom:1.3px solid #555;transform:rotate(45deg)}
.btn-submit{position:absolute;left:110px;top:411px;width:212px;height:46px;background:var(--blue);color:var(--ink);font-size:15px;box-shadow:0 4px 8px rgba(0,0,0,.2)}
.appt-photo{left:598px;top:2746px;width:602px;height:516px;background:linear-gradient(90deg,#2a2a2a 0%,#4a4a4a 50%,#6a6a6a 52%,#8a8a8a 100%)}

/* footer */
.footer{left:0;top:3262px;width:1200px;height:414px;background:var(--grey-footer);color:var(--ink)}
.footer-brand{position:absolute;left:112px;top:92px;font-size:24px}
.footer-about{position:absolute;left:112px;top:212px;width:270px;font-size:13.5px;line-height:24px}
.footer .social{position:absolute;left:112px;top:362px}
.footer-col{position:absolute;top:100px;font-size:14px}
.footer-col h4{font-family:var(--head);font-weight:600;font-size:18px;margin-bottom:22px;white-space:nowrap}
.footer-col li{list-style:none;line-height:34px}
.footer-col .row{display:flex;gap:12px;line-height:26px;margin-bottom:16px}
.bottom{left:0;top:3676px;width:1200px;height:65px;background:var(--grey-bottom);text-align:center;font-size:13.5px;line-height:65px;color:#333}
</style>
</head>
<body>

<header>
  <div class="abs topbar">
    <div class="hours">
      <svg width="12" height="12" viewBox="0 0 12 12"><circle cx="6" cy="6" r="5" fill="none" stroke="#1b1b1b" stroke-width="1.4"/><path d="M6 3v3.2l2 1.2" fill="none" stroke="#1b1b1b" stroke-width="1.3"/></svg>
      We'are Open: Mon - Sat 8:00 - 18:00
    </div>
    <div class="social"><span></span><span></span><span></span><span></span></div>
  </div>
  <div class="abs brand header-brand"><i></i>Brixa Motor Gleam</div>

  <div class="abs contact-item call">
    <svg width="24" height="24" viewBox="0 0 24 24"><path d="M5 2l4 1 1 5-3 2c1.5 3 3.5 5 7 7l2-3 5 1 1 4c-1 2-3 3-5 2C9 19 5 15 3 7 2 5 3 3 5 2z" fill="#e3101e"/></svg>
    <div><b>Call Us</b>+1 888 888 8888</div>
  </div>
  <div class="abs contact-item mail">
    <svg width="30" height="22" viewBox="0 0 30 22"><rect x="1" y="1" width="28" height="20" rx="2" fill="#e3101e"/><path d="M2 3l13 10L28 3" fill="none" stroke="#fff" stroke-width="2"/></svg>
    <div><b>Send us mail</b>BrixaMotorGleam.com</div>
  </div>
  <a class="abs btn btn-book" href="#book">Book Apointment</a>

  <div class="abs underline-red"></div>
  <nav class="abs nav">
    <a class="active" style="left:64px" href="#">Home</a>
    <a style="left:137px" href="#">About</a>
    <a style="left:216px" href="#">Services</a>
    <a style="left:313px" href="#">Why Choose Us</a>
    <a style="left:451px" href="#">Blog</a>
    <a style="left:521px" href="#">Contact</a>
    <div class="tools">
      <svg width="13" height="13" viewBox="0 0 13 13"><circle cx="5.5" cy="5.5" r="4" fill="none" stroke="#fff" stroke-width="2"/><path d="M8.5 8.5l3.5 3.5" stroke="#fff" stroke-width="2"/></svg>
      <span style="display:flex;gap:5px;align-items:center">
        <svg width="11" height="12" viewBox="0 0 11 12"><circle cx="5.5" cy="3" r="3" fill="#fff"/><path d="M0 12c0-4 2.5-5.5 5.5-5.5S11 8 11 12z" fill="#fff"/></svg>LOGIN
      </span>
    </div>
  </nav>
</header>

<section class="abs hero" role="img" aria-label="Engine bay photo split into before and after dry ice cleaning">
  <div class="hero-tag tag-before">BEFORE</div>
  <div class="hero-tag tag-after">AFTER</div>
  <div class="hero-arrow" style="left:22px"><svg width="10" height="14" viewBox="0 0 10 14"><path d="M8 1L2 7l6 6" fill="none" stroke="#fff" stroke-width="1.6"/></svg></div>
  <div class="hero-arrow" style="left:1128px"><svg width="10" height="14" viewBox="0 0 10 14"><path d="M2 1l6 6-6 6" fill="none" stroke="#fff" stroke-width="1.6"/></svg></div>
  <div class="hero-box">
    <h1><span>Brixa</span> Motor Gleam</h1>
    <p>Lorem ipsum dolor sit amet, consectetur adipiscing elit, eiusmod tempor incididunt ut labore et dolore magna aliqua. Ut enim ad minim veniam, quis nostrud exercitation ullamco</p>
    <a class="btn btn-start" href="#">Get Started</a>
  </div>
</section>

<!-- why choose us -->
<h2 class="abs section-title" style="top:855px">Why <span>Choose Us</span></h2>
<div class="abs rule" style="top:921px"></div>

<div class="abs feature" style="left:84px;top:955px">
  <div class="icon"><svg width="44" height="44" viewBox="0 0 44 44" fill="none" stroke="#e3101e" stroke-width="1.6"><circle cx="22" cy="14" r="7"/><path d="M8 40c0-9 6-14 14-14s14 5 14 14"/><path d="M6 8l8 8M38 8l-8 8"/></svg></div>
  <h3>Expert Mechanics</h3>
  <p>Lorem ipsum dolor sit consectetur adipiscing elit, sed do eiusmod tempor incididunt ut labore et</p>
</div>
<div class="abs feature" style="left:350px;top:955px">
  <div class="icon"><svg width="44" height="44" viewBox="0 0 44 44" fill="none" stroke="#e3101e" stroke-width="1.6"><rect x="8" y="13" width="28" height="18" rx="2" transform="rotate(-30 22 22)"/><circle cx="22" cy="22" r="5"/></svg></div>
  <h3>Reasonable Price</h3>
  <p>Lorem ipsum dolor sit consectetur adipiscing elit, sed do eiusmod tempor incididunt ut labore et</p>
</div>
<div class="abs feature" style="left:84px;top:1177px">
  <div class="icon"><svg width="44" height="44" viewBox="0 0 44 44" fill="none" stroke="#e3101e" stroke-width="1.6"><circle cx="22" cy="14" r="8"/><path d="M7 38c0-9 7-13 15-13s15 4 15 13z"/></svg></div>
  <h3>Trusted by 2500+ Clients</h3>
  <p>Lorem ipsum dolor sit consectetur adipiscing elit, sed do eiusmod tempor incididunt ut labore et</p>
</div>
<div class="abs feature" style="left:350px;top:1177px">
  <div class="icon"><svg width="46" height="40" viewBox="0 0 46 40" fill="none" stroke="#e3101e" stroke-width="1.6"><path d="M8 18l5-10h20l5 10"/><rect x="5" y="18" width="36" height="12" rx="3"/><circle cx="13" cy="24" r="2"/><circle cx="33" cy="24" r="2"/><path d="M9 30v5M37 30v5"/></svg></div>
  <h3>Fast feature Delivery</h3>
  <p>Lorem ipsum dolor sit consectetur adipiscing elit, sed do eiusmod tempor incididunt ut labore et</p>
</div>

<div class="abs why-photo" role="img" aria-label="Grey sports car with open hood in a workshop"></div>

<!-- focus area -->
<section class="abs focus">
  <h2 class="abs section-title" style="top:80px">Our <span>Focus Area</span></h2>
  <div class="abs rule" style="top:146px"></div>
  <div class="focus-card" style="left:105px">
    <div class="photo" role="img" aria-label="Vehicle undercarriage close-up" style="background:radial-gradient(circle at 45% 40%,#9a9a9a,#3a3a3a 70%,#1e1e1e)"></div>
    <h3>Undercarriage</h3>
    <p>Lorem ipsum dolor sit amet, consectetur adipiscing elit, sed do eiusmod tempor incididunt ut labore et dolore magna aliqua.</p>
  </div>
  <div class="focus-card" style="left:440px">
    <div class="photo" role="img" aria-label="Hand cleaning an engine bay" style="background:radial-gradient(circle at 55% 45%,#b5b5b5,#555 65%,#262626)"></div>
    <h3>Engine bay</h3>
    <p>Lorem ipsum dolor sit amet, consectetur adipiscing elit, sed do eiusmod tempor incididunt ut labore et dolore magna aliqua.</p>
  </div>
  <div class="focus-card" style="left:777px">
    <div class="photo" role="img" aria-label="Brake disc and wheel hub" style="background:radial-gradient(circle at 50% 50%,#d0d0d0,#7a7a7a 55%,#2a2a2a)"></div>
    <h3>Wheels/wheel wells</h3>
    <p>Lorem ipsum dolor sit amet, consectetur adipiscing elit, sed do eiusmod tempor incididunt ut labore et dolore magna aliqua.</p>
  </div>
</section>

<!-- working process -->
<h2 class="abs section-title" style="top:2315px">Our <span>Working Process</span></h2>
<div class="abs rule" style="top:2381px"></div>

<svg class="abs" style="left:0;top:2400px" width="1200" height="200" viewBox="0 0 1200 200">
  <defs><marker id="ah" markerWidth="10" markerHeight="10" refX="8" refY="5" orient="auto"><path d="M0 0L10 5L0 10z" fill="#8a8a8a"/></marker></defs>
  <path d="M290 75C340 40 430 35 478 98" fill="none" stroke="#8a8a8a" stroke-width="2" stroke-dasharray="2 4" marker-end="url(#ah)"/>
  <path d="M690 145C740 180 820 175 885 130" fill="none" stroke="#8a8a8a" stroke-width="2" stroke-dasharray="2 4" marker-end="url(#ah)"/>
  <circle cx="192" cy="109" r="81" fill="#fff" stroke="#7e9fb6" stroke-width="3"/>
  <circle cx="200" cy="109" r="55" fill="#e3101e"/>
  <circle cx="163" cy="55" r="8" fill="#e3101e"/>
  <rect x="185" y="85" width="28" height="46" rx="4" fill="none" stroke="#fff" stroke-width="2.5"/>
  <path d="M192 98h14M192 106h14M192 114h9" stroke="#fff" stroke-width="2"/>
  <circle cx="590" cy="109" r="81" fill="#fff" stroke="#7e9fb6" stroke-width="3"/>
  <g fill="none" stroke="#e3101e" stroke-width="3"><path d="M578 105l9-18h36l9 18"/><rect x="573" y="105" width="64" height="22" rx="5"/><path d="M580 127v9M630 127v9"/></g>
  <circle cx="1005" cy="109" r="81" fill="#fff" stroke="#7e9fb6" stroke-width="3"/>
  <circle cx="975" cy="55" r="8" fill="#e3101e"/>
  <g fill="none" stroke="#e3101e" stroke-width="3"><circle cx="1008" cy="80" r="16"/><path d="M1008 72l3 6h6l-5 4 2 6-6-4-6 4 2-6-5-4h6z" stroke-width="1.8"/><path d="M983 120l7-14h36l7 14"/><rect x="978" y="120" width="60" height="20" rx="5"/></g>
</svg>
<div class="abs step-num" style="left:104px;top:2440px">1</div>
<div class="abs step-num" style="left:488px;top:2440px">2</div>
<div class="abs step-num" style="left:886px;top:2440px">3</div>
<div class="abs step-label" style="left:76px;top:2598px">Request Quote</div>
<div class="abs step-label" style="left:470px;top:2593px">Bring Your<br>Vehicle</div>
<div class="abs step-label" style="left:875px;top:2593px">Get It<br>Repaired</div>

<!-- appointment -->
<section class="abs appt" id="book">
  <h2>Book An Appointment</h2>
  <div class="rule-left"></div>
  <div class="field" style="left:110px;top:159px;width:214px;height:53px">Name</div>
  <div class="field" style="left:334px;top:159px;width:214px;height:53px">Email</div>
  <div class="field" style="left:110px;top:226px;width:214px;height:53px">Phone</div>
  <div class="field select" style="left:334px;top:226px;width:214px;height:53px">Services</div>
  <div class="field" style="left:110px;top:294px;width:438px;height:90px">Type here</div>
  <div class="btn btn-submit">Submit</div>
</section>
<div class="abs appt-photo" role="img" aria-label="Engine bay shown half dirty and half cleaned"></div>

<!-- footer -->
<footer class="abs footer">
  <div class="brand footer-brand"><i></i>Brixa Motor Gleam</div>
  <p class="footer-about">Lorem ipsum dolor sit amet, adipiscing elit, sed do eiusmod tempor incididunt ut labore et dolore magna aliqua. Ut enim ad minim veniam, quis nostrud exercitation ullamco laboris</p>
  <div class="social"><span></span><span></span><span></span><span></span></div>

  <div class="footer-col" style="left:507px">
    <h4>Quick Links</h4>
    <ul><li>Home</li><li>About us</li><li>Services</li><li>Blog</li><li>Contact</li></ul>
  </div>
  <div class="footer-col" style="left:657px;width:240px">
    <h4>Contact Us</h4>
    <div class="row"><svg width="12" height="26" viewBox="0 0 12 16"><path d="M6 15C2 10 1 7.5 1 6a5 5 0 0110 0c0 1.5-1 4-5 9z" fill="#1b1b1b"/><circle cx="6" cy="6" r="2" fill="#e2e2e2"/></svg><span>Lorem ipsum dolor sit amet, consectetur adipiscing elit,</span></div>
    <div class="row"><svg width="12" height="26" viewBox="0 0 24 24"><path d="M5 2l4 1 1 5-3 2c1.5 3 3.5 5 7 7l2-3 5 1 1 4c-1 2-3 3-5 2C9 19 5 15 3 7 2 5 3 3 5 2z" fill="#1b1b1b"/></svg><span>+1 888 888 8888</span></div>
    <div class="row"><svg width="13" height="26" viewBox="0 0 14 10"><rect width="14" height="10" rx="1" fill="#1b1b1b"/><path d="M1 1l6 5 6-5" fill="none" stroke="#e2e2e2" stroke-width="1.2"/></svg><span>info@BrixaMotorGleam.com</span></div>
  </div>
  <div class="footer-col" style="left:970px">
    <h4>Help Us</h4>
    <ul><li>Support</li><li>Inforamtion</li><li>Legal Policy</li></ul>
  </div>
</footer>
<div class="abs bottom">© 2022 All Rights Reserved</div>

</body>
</html>
```